Single-sided business card for restaurant bellamonte with new logo made on this site

Business card options with new logo including restaurant name, address, phone number and website. This business card is single-sided only and will be presented at the hostess desk for clients to take. I would like to see options based on a cream card background, a white card background, a yellow card background and a burgundy colored background. It needs to be elegant and traditional.

Target Market(s)

local and international crowd

Industry/Entity Type

restaurant

Contact Information for Business Card

address, website and phone number

Font styles to use
Serif

Colors
EE7325
F08F49
F5BC92
FAE3D3
FDF4ED

Requirements
Must have
• new logo, address, phone number, website
Should not have
• more than three colors

```html
<!DOCTYPE html>
<html lang="es">
<head>
<meta charset="utf-8">
<title>Bellamonte – Business Cards</title>
<link rel="stylesheet" href="https://fonts.googleapis.com/css2?family=Cinzel:wght@400;500&display=swap">
<style>
  :root {
    --backdrop: #6e5742;
    --card-yellow: #f0ae28;
    --card-burgundy: #3a191a;
    --burgundy-panel: #361718;
    --ink-dark: #4a1d12;
    --ink-light: #f6eee6;
    --accent-gold: #e6a72a;
  }
  html, body {
    margin: 0;
    padding: 0;
    width: 900px;
    height: 1200px;
    overflow: hidden;
    background: var(--backdrop);
  }
  .canvas {
    position: relative;
    width: 900px;
    height: 1200px;
    font-family: "Cinzel", "Times New Roman", serif;
  }
  .card {
    position: absolute;
    left: 73px;
    width: 777px;
    height: 456px;
  }
  .card--yellow { top: 127px; background: var(--card-yellow); color: var(--ink-dark); }
  .card--burgundy { top: 618px; height: 460px; background: var(--card-burgundy); color: var(--ink-light); }

  .brand-panel {
    position: absolute;
    left: 67px;
    top: 98px;
    width: 253px;
    height: 262px;
  }
  .card--burgundy .brand-panel { background: var(--burgundy-panel); }

  .brand-mark {
    position: absolute;
    left: 68px;
    top: 27px;
    width: 111px;
    height: 111px;
  }
  .card--yellow .brand-mark { background: var(--ink-dark); }
  .card--burgundy .brand-mark { background: var(--ink-light); }

  .brand-name {
    position: absolute;
    left: 0;
    width: 253px;
    top: 152px;
    text-align: center;
    font-size: 27px;
    font-weight: 400;
    letter-spacing: 2px;
    line-height: 1;
  }

  .divider {
    position: absolute;
    left: 366px;
    top: 75px;
    width: 2px;
    height: 306px;
  }
  .card--yellow .divider { background: var(--ink-dark); }
  .card--burgundy .divider { background: var(--accent-gold); }

  .details {
    position: absolute;
    left: 427px;
    top: 82px;
    font-size: 21px;
    line-height: 31px;
    letter-spacing: 0.3px;
  }
  .card--burgundy .details { left: 424px; top: 84px; font-size: 20px; }
  .details p { margin: 0; }
  .rule {
    display: block;
    height: 2px;
    margin: 19px 0 17px;
  }
  .card--yellow .rule { width: 90px; background: var(--ink-dark); }
  .card--burgundy .rule { width: 34px; background: var(--accent-gold); margin: 18px 0 18px; }
</style>
</head>
<body>
<main class="canvas">

  <section class="card card--yellow" aria-label="Bellamonte business card, yellow version">
    <div class="brand-panel">
      <div class="brand-mark"></div>
      <div class="brand-name">BELLAMONTE</div>
    </div>
    <div class="divider"></div>
    <div class="details">
      <p class="details__title">Restaurant Bellamonte</p>
      <span class="rule"></span>
      <p>Magnolia 418</p>
      <p>Bahías de Santa Lucía,</p>
      <p>Oaxaca CP 70912</p>
      <span class="rule"></span>
      <p>Reservaciones</p>
      <p>958-555-0142</p>
      <p>WWW.BELLAMONTE.COM.MX</p>
    </div>
  </section>

  <section class="card card--burgundy" aria-label="Bellamonte business card, burgundy version">
    <div class="brand-panel">
      <div class="brand-mark"></div>
      <div class="brand-name">BELLAMONTE</div>
    </div>
    <div class="divider"></div>
    <div class="details">
      <p class="details__title">Restaurant Bellamonte</p>
      <span class="rule"></span>
      <p>Magnolia 418</p>
      <p>Bahías de Santa Lucía,</p>
      <p>Oaxaca CP 70912</p>
      <span class="rule"></span>
      <p>Reservaciones</p>
      <p>958-555-0142</p>
      <p>WWW.BELLAMONTE.COM.MX</p>
    </div>
  </section>

</main>
</body>
</html>
```